Simple and clean

We need a business card design for a new company called Dwelling Owl. It is a search engine to find current properties for sale or rent in New Zealand market.
We have already a colour scheme that we would like people to use.
Light brown: #D4CCB0
Light green: #D6E4D4
Green: #669966
Black/White
It is OK to divert from this colour scheme slightly as long as there is a green component to the business card.
Final design should be clean, simple and should communicate the nature of the business.
Target Market(s)
- First home buyers
- Real estate agents
- People seeking rentals
Industry/Entity Type
Business
Requirements
Must have
- Use those or similar colours.
Light brown: #D4CCB0
Light green: #D6E4D4
Green: #669966
Black/White

```html
<!DOCTYPE html>
<html lang="en">
<head>
<meta charset="utf-8">
<title>Dwelling Owl – Business Card</title>
<link rel="stylesheet" href="https://fonts.googleapis.com/css2?family=Arimo:wght@400;700&display=swap">
<style>
  :root {
    --page-bg: #ffffff;
    --card-green: #c2e6ba;
    --card-green-light: #d3eecb;
    --panel-green: #b4dcab;
    --panel-green-dark: #a6d29c;
    --ink-green: #4f8250;
    --ink-deep: #2f5a31;
    --mark-green: #1f5a25;
    --shadow: rgba(40, 70, 40, 0.28);
  }
  * { margin: 0; padding: 0; box-sizing: border-box; }
  html, body {
    width: 1200px;
    height: 899px;
    overflow: hidden;
    background: var(--page-bg);
  }
  body {
    position: relative;
    font-family: "Arimo", Arial, sans-serif;
  }
  .business-card {
    position: absolute;
    left: 150px;
    top: 195px;
    width: 900px;
    height: 510px;
    background: linear-gradient(160deg, var(--card-green-light) 0%, var(--card-green) 60%, #b8dfaf 100%);
    box-shadow: 0 10px 30px rgba(0,0,0,0.18);
    overflow: hidden;
  }
  .brand-name {
    position: absolute;
    left: 78px;
    top: 318px;
    transform-origin: left top;
    transform: rotate(-90deg);
    font-size: 44px;
    font-weight: 700;
    color: var(--mark-green);
    white-space: nowrap;
    letter-spacing: -0.5px;
  }
  .brand-dot {
    position: absolute;
    left: 22px;
    top: 368px;
    width: 70px;
    height: 70px;
    border-radius: 50%;
    background: var(--mark-green);
  }
  .holder-name {
    position: absolute;
    left: 230px;
    width: 600px;
    top: 120px;
    text-align: center;
    font-size: 54px;
    font-weight: 700;
    color: var(--ink-green);
    text-shadow: 1px 1px 0 rgba(255,255,255,0.5), -1px -1px 0 rgba(30,60,30,0.35);
  }
  .holder-role {
    position: absolute;
    left: 230px;
    width: 600px;
    top: 183px;
    text-align: center;
    font-size: 30px;
    font-weight: 700;
    color: var(--ink-green);
    text-shadow: 1px 1px 0 rgba(255,255,255,0.5), -1px -1px 0 rgba(30,60,30,0.35);
  }
  .contact-panel {
    position: absolute;
    left: 118px;
    top: 232px;
    width: 810px;
    height: 238px;
    background: linear-gradient(175deg, var(--panel-green) 0%, var(--panel-green-dark) 100%);
    box-shadow: -4px 10px 16px var(--shadow), inset 0 1px 0 rgba(255,255,255,0.4);
  }
  .contact-line {
    position: absolute;
    font-weight: 700;
    color: var(--ink-green);
    text-shadow: 1px 1px 0 rgba(255,255,255,0.45), -1px -1px 0 rgba(30,60,30,0.35);
    white-space: nowrap;
  }
  .contact-phone {
    left: 0;
    width: 560px;
    top: 20px;
    text-align: center;
    font-size: 32px;
    font-weight: 400;
  }
  .contact-email {
    left: 40px;
    top: 72px;
    font-size: 36px;
    font-weight: 400;
    letter-spacing: -0.5px;
  }
  .contact-web {
    left: 0;
    width: 560px;
    top: 168px;
    text-align: center;
    font-size: 36px;
    letter-spacing: -0.5px;
    color: var(--ink-deep);
  }
</style>
</head>
<body>
  <div class="business-card">
    <div class="brand-dot"></div>
    <div class="brand-name">Dwelling Owl</div>

    <div class="holder-name">Sam Carter</div>
    <div class="holder-role">Director</div>

    <div class="contact-panel">
      <div class="contact-line contact-phone">000 000 000</div>
      <div class="contact-line contact-email">sam@dwellingowl.co.nz</div>
      <div class="contact-line contact-web">www.dwellingowl.co.nz</div>
    </div>
  </div>
</body>
</html>
```